Business Card Design Project

My business sells promotional merchandise to large blue chip companies. Gear like polo shirts, drink bottles, pens, basically anything that you can put a company logo onto.

I need the following elements included:
Logo as attached
Peter Hallorand Managing Director
21 Kestrel Court Thornlea 4168
mobile 0438 612054
email tidewell@tidewellcoastal.com.au

Promotional Merchandise with a difference

Mature age Marketing Managers

Business

```html
<!DOCTYPE html>
<html lang="en">
<head>
<meta charset="utf-8">
<title>Tidewell Business Card</title>
<link rel="stylesheet" href="https://fonts.googleapis.com/css2?family=Open+Sans:wght@400;600;700&display=swap">
<style>
  :root {
    --navy: #0c2f63;
    --white: #ffffff;
    --ink: #2b2b2b;
    --card-edge: #d6d6d6;
    --page: #ffffff;
  }
  * { margin: 0; padding: 0; box-sizing: border-box; }
  html, body {
    width: 1200px;
    height: 900px;
    overflow: hidden;
    background: var(--page);
    font-family: "Open Sans", Arial, sans-serif;
  }
  .canvas {
    position: relative;
    width: 1200px;
    height: 900px;
  }
  .card {
    position: absolute;
    top: 290px;
    width: 522px;
    height: 320px;
    border-radius: 10px;
    overflow: hidden;
  }
  .card--front {
    left: 62px;
    background: var(--white);
    border: 2px solid var(--card-edge);
  }
  .card--back {
    left: 614px;
    background: var(--navy);
  }
  .brand-band {
    position: absolute;
    left: 0;
    top: 82px;
    width: 200px;
    height: 52px;
    background: var(--navy);
    display: flex;
    align-items: center;
    justify-content: center;
  }
  .brand-name {
    color: var(--white);
    font-weight: 600;
    letter-spacing: 1px;
    line-height: 1;
  }
  .brand-band .brand-name { font-size: 29px; }
  .person {
    position: absolute;
    left: 232px;
    top: 82px;
    color: var(--ink);
  }
  .person__name {
    font-size: 25px;
    font-weight: 700;
    line-height: 30px;
  }
  .person__role {
    font-size: 15px;
    font-weight: 700;
    line-height: 20px;
  }
  .contact {
    position: absolute;
    left: 232px;
    top: 180px;
    list-style: none;
    color: var(--ink);
    font-size: 14px;
    line-height: 20px;
  }
  .contact__item {
    display: flex;
    align-items: center;
    gap: 6px;
  }
  .contact__icon { width: 11px; height: 12px; flex: none; }
  .card--back .brand-name {
    position: absolute;
    left: 0;
    right: 0;
    top: 160px;
    transform: translateY(-50%);
    text-align: center;
    font-size: 54px;
    letter-spacing: 2px;
  }
</style>
</head>
<body>
<main class="canvas">
  <section class="card card--front" aria-label="Business card front">
    <div class="brand-band"><span class="brand-name">TIDEWELL</span></div>
    <div class="person">
      <p class="person__name">Peter Hallorand</p>
      <p class="person__role">Managing Director</p>
    </div>
    <ul class="contact">
      <li class="contact__item">21 Kestrel Court Thornlea 4168</li>
      <li class="contact__item">
        <svg class="contact__icon" viewBox="0 0 11 12" aria-hidden="true">
          <rect x="2.5" y="0.5" width="6" height="11" rx="1" fill="#2b2b2b"/>
          <rect x="3.5" y="2" width="4" height="5" fill="#ffffff"/>
        </svg>
        0438 612054
      </li>
      <li class="contact__item">
        <svg class="contact__icon" viewBox="0 0 11 12" aria-hidden="true">
          <rect x="0.5" y="3" width="10" height="7" fill="#2b2b2b"/>
          <path d="M0.5 3 L5.5 7 L10.5 3" fill="none" stroke="#ffffff" stroke-width="1"/>
        </svg>
        tidewell@tidewellcoastal.com.au
      </li>
    </ul>
  </section>

  <section class="card card--back" aria-label="Business card back">
    <span class="brand-name">TIDEWELL</span>
  </section>
</main>
</body>
</html>
```